Redesign Event Flyer for Speaker

We are re-designing our professional event flyer template with new headshot and cleaner, up-to-date design. All design details are in PDF file attached. Thank you for participating :)

Font styles to use
Sans Serif

Colors
3276b5
0355a3

Requirements
Must have
• All elements in PDF file.
Nice to have
Should not have
• Tacky or childish elements.

```html
<!DOCTYPE html>
<html lang="en">
<head>
<meta charset="UTF-8">
<title>The Greatest Sale – Speaker Event Flyer</title>
<link href="https://fonts.googleapis.com/css2?family=Bebas+Neue&family=Cinzel:wght@500&family=PT+Serif&display=swap" rel="stylesheet">
<style>
  :root {
    --blue-deep: #0355a3;
    --blue-mid: #3276b5;
    --blue-bright: #0a8fe0;
    --paper: #eef1f4;
    --paper-shade: #d9dfe6;
    --ink: #2b2b2b;
    --brand-red: #d6202f;
    --white: #ffffff;
  }
  * { margin: 0; padding: 0; box-sizing: border-box; }
  html, body { width: 1200px; height: 927px; overflow: hidden; background: var(--paper); }
  .flyer {
    position: relative;
    width: 1200px;
    height: 927px;
    overflow: hidden;
    background: linear-gradient(135deg, #f4f6f8 0%, var(--paper) 45%, var(--paper-shade) 100%);
  }
  .backdrop, .headshot { position: absolute; left: 0; top: 0; width: 1200px; height: 927px; }
  .brand {
    position: absolute;
    left: 43px;
    top: 80px;
    display: flex;
    align-items: center;
    gap: 12px;
    font-family: "Bebas Neue", sans-serif;
    font-size: 46px;
    line-height: 1;
    color: var(--brand-red);
    z-index: 2;
  }
  .brand-mark { width: 26px; height: 26px; background: var(--brand-red); }
  .headline {
    position: absolute;
    left: 41px;
    top: 152px;
    font-family: "Bebas Neue", sans-serif;
    font-weight: 400;
    font-size: 78px;
    line-height: 1;
    color: var(--ink);
    white-space: nowrap;
    z-index: 2;
  }
  .speaker-name {
    position: absolute;
    left: 43px;
    top: 234px;
    font-family: "Cinzel", serif;
    font-weight: 500;
    font-size: 23px;
    line-height: 1;
    color: var(--ink);
    white-space: nowrap;
    z-index: 2;
  }
  .footer-shade {
    position: absolute;
    left: 0; right: 0; bottom: 0;
    height: 230px;
    background: linear-gradient(180deg, rgba(0,0,0,0) 0%, rgba(0,0,0,0.7) 55%, #000 100%);
  }
  .venue {
    position: absolute;
    left: 36px;
    top: 812px;
    display: flex;
    align-items: center;
    gap: 10px;
    width: 180px;
    font-family: "PT Serif", serif;
    font-size: 15px;
    line-height: 1.25;
    color: var(--white);
    z-index: 2;
  }
  .venue-mark { width: 26px; height: 26px; background: var(--white); flex: none; }
  .event-details {
    position: absolute;
    left: 228px;
    top: 794px;
    font-family: "PT Serif", serif;
    font-size: 19px;
    line-height: 31px;
    color: var(--white);
    list-style: none;
    white-space: nowrap;
    z-index: 2;
  }
</style>
</head>
<body>
<div class="flyer">
  <svg class="backdrop" viewBox="0 0 1200 927" aria-hidden="true">
    <defs>
      <linearGradient id="blueField" x1="1" y1="0" x2="0.3" y2="1">
        <stop offset="0" stop-color="#0355a3"/>
        <stop offset="0.5" stop-color="#0a8fe0"/>
        <stop offset="1" stop-color="#0355a3"/>
      </linearGradient>
    </defs>
    <polygon points="0,0 260,0 120,300" fill="#ffffff" opacity="0.35"/>
    <polygon points="380,40 520,230 300,330" fill="#cfd7e0" opacity="0.35"/>
    <polygon points="0,380 210,520 0,700" fill="#ffffff" opacity="0.4"/>
    <polygon points="640,0 820,140 700,260" fill="#d4dbe3" opacity="0.4"/>
    <polygon points="1200,5 750,352 230,752 0,912 0,927 1200,927" fill="url(#blueField)"/>
    <polygon points="1200,5 1200,400 1000,170" fill="#0b4c94" opacity="0.35"/>
    <polygon points="1200,500 1000,700 1200,900" fill="#1aa0ef" opacity="0.25"/>
  </svg>

  <svg class="headshot" viewBox="0 0 1200 927" role="img" aria-label="Black and white portrait of the speaker in a dark suit jacket and white open-collar shirt">
    <defs>
      <radialGradient id="portraitTone" cx="0.53" cy="0.2" r="0.8">
        <stop offset="0" stop-color="#7a7a7a"/>
        <stop offset="0.3" stop-color="#3c3c3c"/>
        <stop offset="1" stop-color="#151515"/>
      </radialGradient>
    </defs>
    <path d="M225,927 L232,560 Q240,470 330,440 L460,380 Q520,340 530,300 L530,60 Q530,8 630,8 Q730,8 730,60 L730,300 Q745,335 800,370 L900,440 Q965,470 970,560 L975,927 Z" fill="url(#portraitTone)"/>
  </svg>

  <div class="footer-shade"></div>

  <div class="brand"><span class="brand-mark"></span>Markwell</div>
  <h1 class="headline">The Greatest Sale</h1>
  <p class="speaker-name">Daniel Everett Ashworth</p>

  <div class="venue"><span class="venue-mark"></span>Harbour Pines Golf Club</div>

  <ul class="event-details">
    <li>Friday, August 9th, 2019</li>
    <li>4200 Lakeshore Pkwy, Port Dalton, Canada</li>
    <li>danieleverettashworth.com | markwell.ca</li>
  </ul>
</div>
</body>
</html>
```